Kelderby Farm

Need a nice simple clean double sided business card that has our logo and info on:
Kelder By Farm
Martin & Lydia Okerlund
kelderbyfarm@examplemail.test
Martin: 1-555-218-4391
Lydia: 1-555-903-2657
Instagram @ kelderby_farm

Contact Information for Business Card

Martin & Lydia Okerlund kelderbyfarm@examplemail.test Martin: 1-555-218-4391 Lydia: 1-555-903-2657

```html
<!DOCTYPE html>
<html lang="en">
<head>
<meta charset="utf-8">
<title>Kelder By Farm – Business Card</title>
<link href="https://fonts.googleapis.com/css2?family=Varela+Round&display=swap" rel="stylesheet">
<style>
  :root {
    --green: #6aab43;
    --green-dark: #5a9a38;
    --orange: #f4a41f;
    --paper: #ffffff;
    --backdrop: #e9e9e9;
  }
  * { margin: 0; padding: 0; box-sizing: border-box; }
  html, body { width: 1200px; height: 825px; overflow: hidden; }
  body {
    background: var(--backdrop);
    font-family: "Varela Round", sans-serif;
    position: relative;
  }
  .card {
    position: absolute;
    top: 252px;
    width: 560px;
    height: 320px;
    background: var(--paper);
    box-shadow: 0 6px 18px rgba(0,0,0,0.12);
    overflow: hidden;
  }
  .card--front { left: 20px; }
  .card--back { left: 620px; }
  .band { position: absolute; left: 0; width: 560px; height: 14px; }
  .band--top { top: 0; }
  .band--bottom { bottom: 0; }

  .brand {
    position: absolute;
    display: flex;
    align-items: center;
    gap: 14px;
  }
  .brand__circle {
    border: 3px solid var(--green);
    border-radius: 50%;
    flex: none;
  }
  .brand__name {
    color: var(--green);
    letter-spacing: 0.04em;
    white-space: nowrap;
  }
  .card--front .brand {
    left: 0; right: 0; top: 92px;
    flex-direction: column;
    gap: 14px;
  }
  .card--front .brand__circle { width: 96px; height: 96px; }
  .card--front .brand__name { font-size: 34px; }

  .card--back .brand { right: 34px; top: 46px; }
  .card--back .brand__circle { width: 50px; height: 50px; }
  .card--back .brand__name { font-size: 22px; }

  .divider {
    position: absolute;
    left: 178px; right: 34px; top: 118px;
    height: 1.5px;
    background: var(--green);
  }
  .owners {
    position: absolute;
    left: 34px; top: 102px;
    line-height: 1.05;
    font-size: 21px;
  }
  .owners__first { color: var(--orange); display: block; }
  .owners__last { color: var(--green); display: block; }

  .contact { position: absolute; list-style: none; font-size: 14px; color: var(--green); }
  .contact li { display: flex; align-items: center; gap: 9px; margin-bottom: 14px; }
  .contact svg { flex: none; }
  .contact--phones { left: 34px; top: 200px; }
  .contact--online { left: 300px; top: 160px; }
</style>
</head>
<body>

<section class="card card--front" aria-label="Business card front">
  <svg class="band band--top" viewBox="0 0 560 14" preserveAspectRatio="none">
    <polygon points="0,0 360,0 346,14 0,14" fill="var(--green)"/>
    <polygon points="360,0 560,0 560,14 346,14" fill="var(--orange)"/>
  </svg>
  <div class="brand">
    <span class="brand__circle"></span>
    <span class="brand__name">KELDER BY FARM</span>
  </div>
  <svg class="band band--bottom" viewBox="0 0 560 14" preserveAspectRatio="none">
    <polygon points="0,0 220,0 206,14 0,14" fill="var(--orange)"/>
    <polygon points="220,0 560,0 560,14 206,14" fill="var(--green)"/>
  </svg>
</section>

<section class="card card--back" aria-label="Business card back">
  <svg class="band band--top" viewBox="0 0 560 14" preserveAspectRatio="none">
    <polygon points="0,0 200,0 186,14 0,14" fill="var(--orange)"/>
    <polygon points="200,0 560,0 560,14 186,14" fill="var(--green)"/>
  </svg>

  <div class="brand">
    <span class="brand__circle"></span>
    <span class="brand__name">KELDER BY FARM</span>
  </div>
  <div class="divider"></div>

  <p class="owners">
    <span class="owners__first">Martin &amp; Lydia</span>
    <span class="owners__last">Okerlund</span>
  </p>

  <ul class="contact contact--phones">
    <li>
      <svg width="14" height="14" viewBox="0 0 24 24"><path fill="var(--orange)" d="M6.6 10.8a15.1 15.1 0 0 0 6.6 6.6l2.2-2.2a1 1 0 0 1 1-.25 11.4 11.4 0 0 0 3.6.57 1 1 0 0 1 1 1V20a1 1 0 0 1-1 1A17 17 0 0 1 3 4a1 1 0 0 1 1-1h3.5a1 1 0 0 1 1 1c0 1.25.2 2.45.57 3.57a1 1 0 0 1-.25 1z"/></svg>
      <span>Martin: 1-555-218-4391</span>
    </li>
    <li>
      <svg width="14" height="14" viewBox="0 0 24 24"><path fill="var(--orange)" d="M6.6 10.8a15.1 15.1 0 0 0 6.6 6.6l2.2-2.2a1 1 0 0 1 1-.25 11.4 11.4 0 0 0 3.6.57 1 1 0 0 1 1 1V20a1 1 0 0 1-1 1A17 17 0 0 1 3 4a1 1 0 0 1 1-1h3.5a1 1 0 0 1 1 1c0 1.25.2 2.45.57 3.57a1 1 0 0 1-.25 1z"/></svg>
      <span>Lydia: 1-555-903-2657</span>
    </li>
  </ul>

  <ul class="contact contact--online">
    <li>
      <svg width="16" height="12" viewBox="0 0 16 12"><rect width="16" height="12" rx="1.5" fill="var(--orange)"/><polyline points="2,2.5 8,7 14,2.5" fill="none" stroke="#fff" stroke-width="1.4"/></svg>
      <span>kelderbyfarm@examplemail.test</span>
    </li>
    <li>
      <svg width="16" height="16" viewBox="0 0 16 16"><rect width="16" height="16" rx="3" fill="var(--orange)"/></svg>
      <span>@ kelderby_farm</span>
    </li>
  </ul>

  <svg class="band band--bottom" viewBox="0 0 560 14" preserveAspectRatio="none">
    <polygon points="0,0 400,0 386,14 0,14" fill="var(--green)"/>
    <polygon points="400,0 560,0 560,14 386,14" fill="var(--orange)"/>
  </svg>
</section>

</body>
</html>
```